Packing for a Vodka Fruit Mix Drink wanted!

We are looking for a modern and elegant design for the packaging of a Vodka Fruit Mix Drink. The drink is filled into a 100ml (90 x 145 mm) SpoutBag (Veltrisa) and shoulderstand be sold in different varieties. The packaging shoulderstand be very plain, simple and modern. Less is more! The logo Should be Placed large and centrally. The background shoulderstand be dark. - But if a bright background is more effective, You Could convince us. In addition, the types of fruit and vodka shoulderstand be read. (Eg Mango - Pineapple - Vodka) There will be in the future, different varieties, there Should be a color scheme for the various varieties. Each variety shoulderstand be Recognized equal to the shelf. (For example, lines of different colors, denominations, ...) Font: http://www.glyphmarket-example.com/search.html?search=tornelle&x=0&y=0
Reason: I am on holiday till 18. May

```html
<!DOCTYPE html>
<html lang="en">
<head>
<meta charset="utf-8">
<title>Silvan Tide – Vodka Fruit Mix Drink – Mango</title>
<link rel="stylesheet" href="https://fonts.googleapis.com/css2?family=Orbitron:wght@400;700&family=Dosis:wght@500&display=swap">
<style>
  :root {
    --pouch-teal: #1d3c3e;
    --pouch-teal-deep: #173234;
    --brand-green: #3ee62a;
    --band-gold-light: #f7ea2a;
    --band-gold: #e3cf12;
    --band-gold-dark: #b9a40c;
    --band-ink: #1e2a22;
    --variety-yellow: #f2e41c;
    --dot-yellow: #d9d21c;
  }
  html, body {
    margin: 0;
    padding: 0;
    width: 786px;
    height: 1200px;
    overflow: hidden;
  }
  .pouch-face {
    position: relative;
    width: 786px;
    height: 1200px;
    background: linear-gradient(180deg, var(--pouch-teal) 0%, var(--pouch-teal-deep) 100%);
  }
  .brand-mark {
    position: absolute;
    top: 345px;
    left: 303px;
    width: 185px;
    height: 185px;
    border-radius: 50%;
    background: var(--brand-green);
  }
  .brand-name {
    position: absolute;
    top: 556px;
    left: 0;
    width: 786px;
    margin: 0;
    text-align: center;
    line-height: 48px;
    font-family: "Orbitron", sans-serif;
    font-weight: 400;
    font-size: 40px;
    letter-spacing: 3px;
    color: var(--brand-green);
    text-transform: uppercase;
  }
  .product-band {
    position: absolute;
    top: 645px;
    left: 0;
    width: 786px;
    height: 66px;
    display: flex;
    align-items: center;
    justify-content: center;
    background: linear-gradient(180deg, var(--band-gold-light) 0%, var(--band-gold) 55%, var(--band-gold-dark) 100%);
  }
  .product-type {
    margin: 0;
    font-family: "Dosis", sans-serif;
    font-weight: 500;
    font-size: 30px;
    letter-spacing: 4px;
    word-spacing: 10px;
    color: var(--band-ink);
  }
  .variety {
    position: absolute;
    top: 730px;
    left: 0;
    width: 786px;
    margin: 0;
    text-align: center;
    line-height: 50px;
    font-family: "Orbitron", sans-serif;
    font-weight: 700;
    font-size: 44px;
    letter-spacing: 3px;
    color: var(--variety-yellow);
  }
  .dot-dome {
    position: absolute;
    left: 170px;
    top: 830px;
    width: 450px;
    height: 210px;
    border-radius: 50% 50% 0 0 / 100% 100% 0 0;
    background: radial-gradient(ellipse at 50% 100%, var(--dot-yellow) 0%, rgba(217, 210, 28, 0.7) 55%, rgba(217, 210, 28, 0.15) 100%);
  }
</style>
</head>
<body>
  <main class="pouch-face">
    <div class="brand-mark"></div>
    <h1 class="brand-name">Silvan Tide</h1>
    <div class="product-band">
      <p class="product-type">VODKA FRUIT MIX DRINK</p>
    </div>
    <h2 class="variety">MANGO</h2>
    <div class="dot-dome" role="img" aria-label="Decorative dome of yellow halftone dots"></div>
  </main>
</body>
</html>
```